Design a cover that embodies the concept of healing by Walking Out of the Fog

Subtitle: How to use tapping, applied kinesiology, and Chinese medicine to heal your body, free your mind and live in peace.

Tapping (Emotional Freedom Technique) is a modern mix of psychology and Chinese medicine that helps people to release the emotions they have inside that are contributing to the depression and anxiety they feel. Applied kinesiology or muscle testing is a biofeedback tool which helps to extract information from the body that can help people to profoundly heal. It can be used to determine whether heavy metals, heavy chemicals, food sensitivities or pathogens are causing the body problems. It can also be used to determine which supplements can help someone heal. This tool also can be used to identify emotions and memories that are also causing someone problems. Lastly, Chinese medicine uses food therapy, herbal formulas, meditation, tai chi (meditative movement), cupping and other tools to help people to be free of depression. This book is written to be information but also details my own personal journey of how I was able to heal from 11 years of heavy depression through the use of these tools.

The heart of the book is about emotional release, emotional freedom and emotional healing. You can surrender, release or let go of emotions and feel better very quickly. This certainly was my experience.

I would like the front and back cover to each be 8.5" x 5.5". I still have to get an ISBN number for the back page as well. Here is the text that I would like on the back cover for now: Millions of people feel the pain, loneliness, and agony of anxiety and depression every day. Many turn to Western medicine in the hopes that a pill will ease the pain and make the problem go away. Oftentimes, this only makes matters worse and doesn’t address the root cause. No one should have to struggle like this when natural answers exist that can address the physical, energetic, emotional, or spiritual causes of anxiety and depression. For 11 long years, Dr. Vance personally struggled with heavy depression until he discovered answers that helped him to completely heal. Walking Out of the Fog is a guide that will help you discover - The two root physical causes of depression and exactly what to do to start healing today - How the negative emotions we have stored within from trauma and bad experiences can drive depression - Tools from Chinese medicine, applied kinesiology, and tapping to help you free your mind and live in peace - An actionable plan to help you let go of the pain, suffering, and negative emotions from your past Whether you feel depressed and anxious or know someone who struggles with these issues, Walking Out of the Fog will transform how you think about depression and will give you the tools to heal so that you can be free and live in peace. Dr. Vance Holbrook is a board-certified acupuncture physician licensed in the state of Florida. He received his training at the Calder Institute of Holistic Practice. He also graduated with a master’s degree in counseling and psychology from Meadowbrook Seminary of Theology. His mission is to help people transform their health and improve the quality of their life naturally. He lives in Orlando, FL where he runs a holistic medical clinic called Bluepine Wellness Center. www.drvanceholbrook-example.com Picstream: drvanceholbrook Friendline: bluepinewellnesscenter

Target Market(s)

Those who suffer from depression and anxiety and want to heal naturally

Industry/Entity Type

Health And Wellness

Requirements
Must have
• My picture should be small and go on the back cover next to the information about me. The front cover would be all graphical. Thank you. On the front cover my name should be posted as "Dr. Vance Holbrook, AP, MA"

```html
<!DOCTYPE html>
<html lang="en">
<head>
<meta charset="utf-8">
<title>Walking Out of the Fog – Book Cover</title>
<link rel="stylesheet" href="https://fonts.googleapis.com/css2?family=Oswald:wght@300;400&family=Roboto+Condensed:wght@400;700&family=Source+Sans+3:ital,wght@0,600;0,700;1,700&family=Noto+Serif+SC:wght@400&display=swap">
<style>
  :root {
    --stage: #c9cfd0;
    --title-green: #3f9a2a;
    --title-gray: #4a4d50;
    --subtitle-ink: #2e3236;
    --author-white: #ffffff;
    --back-top: #4d6068;
    --back-mid: #39474d;
    --back-bottom: #2a3236;
    --body-white: #f2f4f4;
    --bullet-red: #e0322b;
    --name-green: #58c23a;
    --spine: #2f393d;
    --glyph-teal: rgba(70, 150, 140, 0.45);
  }
  * { box-sizing: border-box; margin: 0; padding: 0; }
  html, body { width: 1200px; height: 800px; overflow: hidden; }
  body { background: var(--stage); position: relative; font-family: "Roboto Condensed", "Arial Narrow", sans-serif; }

  .book-wrap { position: absolute; left: 106px; top: 44px; display: flex; gap: 24px; height: 712px; }

  /* Front cover */
  .front-cover { position: relative; width: 460px; height: 712px; overflow: hidden; }
  .front-photo { position: absolute; inset: 0;
    background: linear-gradient(180deg, #5aa6e0 0%, #a9d3f0 28%, #dfeef6 40%, #b9cfa4 46%, #7fb04a 58%, #5e9a2e 80%, #4d8424 100%); }
  .front-title { position: absolute; left: 26px; top: 20px; width: 420px; }
  .title-lead { font-family: "Source Sans 3", sans-serif; font-style: italic; font-weight: 700; font-size: 22px; color: var(--title-green); }
  .title-main { font-family: "Source Sans 3", sans-serif; font-weight: 700; font-size: 64px; line-height: 0.95; color: var(--title-gray); margin-left: 150px; letter-spacing: -0.5px; }
  .front-subtitle { position: absolute; left: 226px; top: 112px; width: 222px; text-align: center;
    font-family: "Source Sans 3", sans-serif; font-weight: 600; font-size: 17px; line-height: 1.18; color: var(--subtitle-ink); }
  .qi-glyphs { position: absolute; left: 342px; top: 238px; writing-mode: vertical-rl;
    font-family: "Noto Serif SC", serif; font-size: 48px; color: var(--glyph-teal); letter-spacing: 16px; }
  .front-author { position: absolute; left: 0; right: 0; bottom: 26px; text-align: center;
    font-family: "Oswald", sans-serif; font-weight: 300; font-size: 31px; color: var(--author-white); letter-spacing: 0.5px; }

  /* Back cover */
  .back-cover { position: relative; width: 460px; height: 712px; overflow: hidden; color: var(--body-white); }
  .back-photo { position: absolute; inset: 0;
    background: linear-gradient(180deg, var(--back-top) 0%, var(--back-mid) 45%, #4a5554 70%, var(--back-bottom) 100%); }
  .back-content { position: relative; padding: 22px 22px 0 22px; }
  .back-title { display: flex; align-items: baseline; gap: 10px; margin-left: 4px; }
  .back-title .title-lead { font-size: 16px; }
  .back-title .title-main { font-size: 38px; margin: 0; color: #e6e9ea; }
  .back-body { margin-top: 14px; font-size: 11.6px; line-height: 1.26; }
  .back-body p { margin-bottom: 12px; }
  .feature-list { list-style: none; margin: 0 0 12px; }
  .feature-list li { position: relative; padding-left: 10px; }
  .feature-list li::before { content: ""; position: absolute; left: 0; top: 5px; width: 5px; height: 5px; border-radius: 50%; background: var(--bullet-red); }
  .author-bio { display: flex; gap: 10px; margin-top: 20px; font-size: 11.6px; line-height: 1.26; }
  .author-portrait { flex: 0 0 64px; height: 72px; background: linear-gradient(160deg, #cfd8c8, #8c9a86); border: 1px solid #e8e8e8; }
  .author-name { color: var(--name-green); font-weight: 700; }
  .contact-list { list-style: none; margin-top: 60px; font-size: 11px; font-weight: 700; line-height: 1.6; }

  /* Spine */
  .spine { position: relative; width: 44px; height: 712px; margin-left: -24px; background: linear-gradient(90deg, #3a464b, var(--spine)); }
  .spine-title, .spine-author { position: absolute; left: 50%; writing-mode: vertical-rl; transform: translateX(-50%); white-space: nowrap; }
  .spine-title { top: 22px; display: flex; align-items: center; gap: 8px; }
  .spine-title .title-lead { font-size: 13px; }
  .spine-title .title-main { font-size: 28px; margin: 0; color: #e6e9ea; }
  .spine-author { bottom: 24px; font-family: "Oswald", sans-serif; font-weight: 300; font-size: 18px; color: #e6e9ea; }
</style>
</head>
<body>
<div class="book-wrap">

  <section class="front-cover">
    <div class="front-photo" role="img" aria-label="Photograph of a woman meditating cross-legged in a green meadow under a blue sky"></div>
    <h1 class="front-title">
      <div class="title-lead">Walking Out of the</div>
      <div class="title-main">Fog</div>
    </h1>
    <p class="front-subtitle">How to use tapping, applied kinesiology, and Chinese medicine to heal your body, free your mind and live in peace.</p>
    <div class="qi-glyphs" aria-hidden="true">养氣</div>
    <div class="front-author">DR. VANCE HOLBROOK, AP, MA</div>
  </section>

  <section class="back-cover">
    <div class="back-photo" role="img" aria-label="Faded photograph of a person meditating on a shore in muted blue-gray tones"></div>
    <div class="back-content">
      <h2 class="back-title"><span class="title-lead">Walking Out of the</span><span class="title-main">Fog</span></h2>
      <div class="back-body">
        <p>Millions of people feel the pain, loneliness, and agony of anxiety and depression every day. Many turn to Western medicine in the hopes that a pill will ease the pain and make the problem go away. Oftentimes, this only makes matters worse and doesn’t address the root cause. No one should have to struggle like this when natural answers exist that can address the physical, energetic, emotional, or spiritual causes of anxiety and depression.</p>
        <p style="margin-bottom:0">For 11 long years, Dr. Vance personally struggled with heavy depression until he discovered answers that helped him to completely heal. Walking Out of the Fog is a guide that will help you discover:</p>
        <ul class="feature-list">
          <li>The two root physical causes of depression and exactly what to do to start healing today</li>
          <li>How the negative emotions we have stored within from trauma and bad experiences can drive depression</li>
          <li>Tools from Chinese medicine, applied kinesiology, and tapping to help you free your mind and live in peace</li>
          <li>An actionable plan to help you let go of the pain, suffering, and negative emotions from your past</li>
        </ul>
        <p>Whether you feel depressed and anxious or know someone who struggles with these issues, Walking Out of the Fog will transform how you think about depression and will give you the tools to heal so that you can be free and live in peace.</p>
      </div>
      <div class="author-bio">
        <div class="author-portrait" role="img" aria-label="Small portrait photo of the author"></div>
        <p><span class="author-name">Dr. Vance Holbrook</span> is a board-certified acupuncture physician licensed in the state of Florida. He received his training at the Calder Institute of Holistic Practice. He also graduated with a master’s degree in counseling and psychology from Meadowbrook Seminary of Theology. His mission is to help people transform their health and improve the quality of their life naturally. He lives in Orlando, FL where he runs a holistic medical clinic called Bluepine Wellness Center.</p>
      </div>
      <ul class="contact-list">
        <li>www.drvanceholbrook-example.com</li>
        <li>Picstream: drvanceholbrook</li>
        <li>Friendline: bluepinewellnesscenter</li>
      </ul>
    </div>
  </section>

  <section class="spine">
    <div class="spine-title"><span class="title-lead">Walking Out of the</span><span class="title-main">Fog</span></div>
    <div class="spine-author">DR. VANCE HOLBROOK, AP, MA</div>
  </section>

</div>
</body>
</html>
```